New web page design for our brand Casa Lunares

We have changed our logo and the image of our products, so we would like to redesign ,our web page as well according to the new design.
Our cosmetic products are based in nature and tradition, like they used to be prepared in the old pharmacies.
Our actual web is www.casalunaresweb.es, so we need similar estructure but completely different design.

Industry/Entity Type

Cosmetics

Number of Pages Required

5+ page

Requirements
Must have
• References to natural ingredients and also to old pharmacys or apothecaries.
Nice to have
• Nature images or old botanics drawings
• I would like to have a cover page with just an image saying welcome to Casa Lunares's world

```html
<!DOCTYPE html>
<html lang="es">
<head>
<meta charset="utf-8">
<title>Casa Lunares – Only Organic Formulas Magistrales</title>
<link href="https://fonts.googleapis.com/css2?family=Lato:wght@300;400;700;900&display=swap" rel="stylesheet">
<style>
:root{
  --ink:#333333;
  --muted:#8a8a8a;
  --brown-dark:#3a2b27;
  --brown-mid:#5a4038;
  --nav:#4b4646;
  --nav-dark:#2f2b2b;
  --green:#8cc63f;
  --sale:#e32626;
  --panel:#f3f3f3;
  --line:#e2e2e2;
  --news:#858080;
  --footer:#221c1b;
  --footer-bottom:#141111;
  --blue:#3b6fc4;
  --sky:#3fa9e0;
  --teal:#1f5f7a;
  --red:#e53a3a;
}
*{box-sizing:border-box;margin:0;padding:0}
html,body{width:1200px;height:3272px;overflow:hidden}
body{font-family:"Lato",sans-serif;color:var(--ink);background:#fff;position:relative}
.section{position:absolute;left:0;width:1200px}
a{color:inherit;text-decoration:none}

/* header */
.site-header{top:0;height:140px}
.brand{position:absolute;left:60px;top:34px;display:flex;align-items:center;gap:10px}
.brand-mark{width:46px;height:46px;border-radius:50%;background:var(--brown-dark)}
.brand-name{font-size:24px;font-weight:900;color:var(--brown-dark);letter-spacing:.5px}
.search{position:absolute;left:388px;top:58px;display:flex}
.search-input{width:300px;height:28px;border:1px solid #cfcfcf;font-size:11px;color:#aaa;padding:7px 10px}
.search-btn{width:70px;height:28px;background:var(--brown-dark);color:#fff;font-size:10px;font-weight:700;display:flex;align-items:center;justify-content:center}
.top-links{position:absolute;right:48px;top:16px;font-size:11px;font-weight:700;color:#444;display:flex;gap:14px}
.top-links span+span::before{content:"|";margin-right:14px;color:#bbb}
.cart-row{position:absolute;right:48px;top:70px;display:flex;gap:20px;font-size:11px;color:#555;align-items:center}
.cart-row svg{vertical-align:middle}

/* nav */
.main-nav{top:140px;height:48px;background:var(--nav);display:flex;align-items:center;padding:0 48px}
.main-nav ul{list-style:none;display:flex;gap:34px;font-size:11px;font-weight:700;color:#e9e6e6;letter-spacing:.5px}
.checkout{margin-left:auto;background:var(--nav-dark);color:#fff;font-size:11px;font-weight:700;height:48px;padding:0 22px;display:flex;align-items:center}

/* hero */
.hero{top:188px;height:470px;background:linear-gradient(#fafafa,#efefef)}
.hero-copy{position:absolute;left:48px;top:90px;width:460px}
.hero-title{font-size:52px;font-weight:900;color:#222;line-height:1;letter-spacing:1px}
.hero-sub{font-size:42px;font-weight:300;color:#333;margin-top:8px;letter-spacing:1px}
.hero-text{font-size:13px;color:#666;line-height:1.5;margin-top:18px}
.btn-dark{display:inline-block;background:var(--brown-dark);color:#fff;font-size:11px;font-weight:700;padding:10px 20px;margin-top:22px;letter-spacing:.5px}
.hero-photo{position:absolute;left:520px;top:70px;width:640px;height:330px;background:radial-gradient(ellipse at 50% 60%,#ffffff 0%,#ece8e6 60%,#e2dcd8 100%);border-radius:4px}
.dots{position:absolute;left:56px;top:428px;display:flex;gap:8px}
.dots span{width:10px;height:10px;border-radius:50%;border:2px solid #555}
.dots span:first-child{background:#555}

/* features */
.features{top:712px;height:96px;background:var(--panel);display:flex;align-items:center}
.feature{flex:1;display:flex;align-items:center;justify-content:center;gap:14px;border-right:1px solid var(--line);height:56px}
.feature:last-child{border-right:0}
.feature-title{font-size:14px;font-weight:900;color:#333}
.feature-note{font-size:11px;color:var(--muted)}

/* promos */
.promos{top:852px;height:400px}
.promo-arrivals{position:absolute;left:48px;top:0;width:424px;height:400px;background:var(--brown-dark);padding:18px}
.promo-frame{border:1px solid #6d5750;height:100%;display:flex;flex-direction:column;align-items:center;justify-content:center;text-align:center;color:#fff;padding:0 40px}
.promo-frame h2{font-size:54px;font-weight:900;line-height:1.05;letter-spacing:1px}
.promo-frame p{font-size:12px;color:#d7cbc6;line-height:1.5;margin-top:16px}
.btn-light{background:#fff;color:var(--brown-dark);font-size:11px;font-weight:900;padding:14px 26px;margin-top:26px}
.promo-sale{position:absolute;left:508px;top:0;width:652px;height:400px;background:linear-gradient(135deg,#7a5636,#b8844e 50%,#5d3e28)}
.sale-copy{position:absolute;left:0;right:0;top:70px;text-align:center;color:#fff}
.sale-copy h2{font-size:46px;font-weight:900;line-height:1.1;letter-spacing:1px}
.sale-copy p{font-size:12px;color:#f1e6dc;margin:14px auto 0;width:420px;line-height:1.5}
.sale-copy .btn-dark{margin-top:26px;padding:14px 26px}

/* products */
.products{top:1320px;height:640px}
.section-head{position:absolute;left:48px;right:48px;top:20px;display:flex;align-items:center;border-bottom:1px solid var(--line);padding-bottom:12px}
.section-head h3{font-size:22px;font-weight:400;color:#222}
.section-head h3 b{font-weight:900}
.filters{margin-left:auto;display:flex;gap:16px;font-size:10px;color:#777}
.filters span{border:1px solid #ddd;padding:4px 10px}
.filters span:first-child{color:var(--green);border-color:var(--green)}
.product-grid{position:absolute;left:48px;top:100px;display:flex;gap:36px}
.product-card{width:251px;height:460px;border:1px solid var(--line);position:relative;padding:0 18px}
.product-photo{height:180px;margin:14px 0 0;background:radial-gradient(circle,#f4eef0,#ffffff 70%)}
.sale-badge{position:absolute;right:12px;top:8px;background:var(--sale);color:#fff;font-size:9px;font-weight:700;padding:3px 6px}
.price{margin-top:26px;font-size:40px;font-weight:400;color:#222}
.price s{font-size:14px;color:#999;margin-left:8px}
.product-name{font-size:13px;font-weight:900;margin-top:12px}
.product-desc{font-size:11px;color:#777;line-height:1.5;margin-top:6px}
.card-actions{position:absolute;left:18px;bottom:22px;display:flex;gap:16px}
.act-cart{width:44px;height:40px;display:flex;align-items:center;justify-content:center}
.act-cart.dark{background:var(--brown-dark)}
.act-cart.green{background:var(--green)}
.act-more{width:88px;height:40px;background:#e9e9e9;font-size:12px;color:#444;display:flex;align-items:center;justify-content:center}
.pager{position:absolute;right:48px;top:600px;display:flex;gap:6px;font-size:11px}
.pager span{border:1px solid #ccc;height:24px;min-width:24px;display:flex;align-items:center;justify-content:center;padding:0 6px;color:#555}
.pager .on{background:var(--nav-dark);color:#fff;border-color:var(--nav-dark)}
.pager .wide{padding:0 14px}

/* categories */
.categories{top:2020px;height:312px;display:flex;gap:20px;padding:0 48px}
.tile{flex:1;position:relative}
.tile-natural{background:linear-gradient(135deg,#3d3a22,#6c6b3a 55%,#2e2b1b)}
.tile-family{background:linear-gradient(135deg,#d9cfae,#a9a25a 50%,#77802f)}
.tile-geriatric{background:linear-gradient(135deg,#6e5a1f,#c9a23c 50%,#4b3f18)}
.natural-copy{position:absolute;left:28px;top:104px;color:#fff}
.natural-copy h4{font-size:28px;font-weight:400;letter-spacing:1px}
.natural-copy p{font-size:11px;color:#e4e0cf;line-height:1.5;width:230px;margin-top:8px}
.natural-copy .btn-light{display:inline-block;padding:7px 14px;margin-top:14px;font-size:9px}
.tile-band{position:absolute;left:0;right:0;bottom:40px;height:48px;background:rgba(40,30,28,.85);color:#fff;font-size:22px;font-weight:400;display:flex;align-items:center;justify-content:center;letter-spacing:1px}

/* newsletter */
.newsletter{top:2364px;height:190px;background:var(--news);display:flex;align-items:center;padding:0 48px}
.newsletter-copy h3{font-size:36px;font-weight:400;color:#fff}
.newsletter-copy p{font-size:11px;color:#ece8e8;line-height:1.5;margin-top:6px;width:300px}
.newsletter-form{margin-left:auto;display:flex}
.news-input{width:580px;height:64px;background:#6b6666;color:#cfcaca;font-size:12px;display:flex;align-items:center;padding:0 20px}
.news-btn{width:170px;height:64px;background:var(--brown-dark);color:#fff;font-size:17px;font-weight:900;display:flex;align-items:center;justify-content:center;letter-spacing:1px}

/* social */
.social{top:2592px;height:190px;text-align:center}
.social h3{font-size:20px;font-weight:900;color:#222;margin-top:24px}
.social-row{display:flex;justify-content:center;gap:60px;margin-top:26px}
.social-item{width:200px}
.social-btn{height:42px;color:#fff;font-size:15px;font-weight:700;display:flex;align-items:center;justify-content:center;gap:10px}
.social-btn i{width:10px;height:10px;background:#fff;display:inline-block}
.social-count{font-size:10px;color:#888;margin-top:8px}
.fb{background:var(--blue)}.tw{background:var(--sky)}.li{background:var(--teal)}.gp{background:var(--red)}

/* guarantees */
.guarantees{top:2800px;height:132px;background:var(--brown-dark);display:flex;align-items:center;padding:0 48px}
.guarantee{flex:1;display:flex;align-items:center;justify-content:center;gap:18px;color:#fff;border-right:1px solid #5b4a45;height:64px}
.guarantee:last-child{border-right:0}
.guarantee b{display:block;font-size:15px;font-weight:900;line-height:1.3}

/* footer */
.site-footer{top:2932px;height:300px;background:var(--footer);display:flex;padding:46px 48px 0;gap:40px;color:#bdb6b4}
.footer-col{flex:1}
.footer-col h5{font-size:12px;font-weight:900;color:#fff;letter-spacing:.5px;margin-bottom:16px}
.footer-col li{list-style:none;font-size:11px;line-height:1.8}
.contact-line{display:flex;gap:10px;font-size:11px;line-height:1.5;margin-bottom:12px;align-items:flex-start}
.footer-bottom{top:3232px;height:40px;background:var(--footer-bottom);display:flex;align-items:center;padding:0 48px;font-size:11px;color:#9a9391}
.cards{margin-left:auto;display:flex;gap:8px}
.cards span{width:34px;height:22px;border-radius:3px}
</style>
</head>
<body>

<header class="section site-header">
  <div class="brand"><span class="brand-mark"></span><span class="brand-name">Casa Lunares</span></div>
  <div class="search"><div class="search-input">Search here</div><div class="search-btn">SEARCH</div></div>
  <div class="top-links"><span>LOGIN/REGISTER</span><span>MY WISHLIST</span><span>WISHLIST</span></div>
  <div class="cart-row">
    <span><svg width="16" height="14" viewBox="0 0 16 14"><path d="M1 1h3l2 8h8l1-6H5" fill="none" stroke="#555" stroke-width="1.5"/><circle cx="7" cy="12" r="1.3" fill="#555"/><circle cx="13" cy="12" r="1.3" fill="#555"/></svg> CART · 0 items</span>
    <span>€ Currency ▾</span>
  </div>
</header>

<nav class="section main-nav">
  <ul><li>⌂ HOME</li><li>ABOUT</li><li>NEWS</li><li>LAB</li><li>FOR HER</li><li>FOR WOMEN</li><li>SERVICES</li><li>TESTIMONIALS</li><li>CONTACT US</li></ul>
  <div class="checkout">CHECKOUT</div>
</nav>

<section class="section hero">
  <div class="hero-copy">
    <h1 class="hero-title">ONLY ORGANIC</h1>
    <p class="hero-sub">FORMULAS MAGISTRALES</p>
    <p class="hero-text">Lorem ipsum dolor sit amet, consectetur adipiscing elit, sed do eiusmod tempor incididunt ut labore et dolore magna aliqua. Ut enim ad minim veniam quis nostrud.</p>
    <a class="btn-dark">READ MORE</a>
  </div>
  <div class="hero-photo" role="img" aria-label="Row of jars, bottles and tubes of the organic cosmetics range"></div>
  <div class="dots"><span></span><span></span><span></span><span></span></div>
</section>

<section class="section features">
  <div class="feature">
    <svg width="30" height="26" viewBox="0 0 30 26"><path d="M3 12h6v12H3zM9 13l6-10c2 0 3 1 2 5h8c2 0 2 2 1 3l-3 11H9z" fill="none" stroke="#333" stroke-width="2"/></svg>
    <div><div class="feature-title">SATISFACTION</div><div class="feature-note">100% Guaranteed</div></div>
  </div>
  <div class="feature">
    <svg width="34" height="22" viewBox="0 0 34 22"><path d="M1 2h20v14H1zM21 7h7l5 5v4H21z" fill="#333"/><circle cx="8" cy="18" r="3" fill="#333" stroke="#f3f3f3" stroke-width="1.5"/><circle cx="27" cy="18" r="3" fill="#333" stroke="#f3f3f3" stroke-width="1.5"/></svg>
    <div><div class="feature-title">FREE SHIPPING</div><div class="feature-note">on orders over $99</div></div>
  </div>
  <div class="feature">
    <svg width="28" height="28" viewBox="0 0 28 28"><circle cx="14" cy="14" r="11" fill="none" stroke="#333" stroke-width="2"/><path d="M14 7v7l5 3" fill="none" stroke="#333" stroke-width="2"/></svg>
    <div><div class="feature-title">7 DAY</div><div class="feature-note">Easy to Return Items</div></div>
  </div>
  <div class="feature">
    <svg width="28" height="28" viewBox="0 0 28 28"><circle cx="14" cy="14" r="11" fill="none" stroke="#333" stroke-width="2"/><circle cx="14" cy="14" r="4" fill="none" stroke="#333" stroke-width="2"/><path d="M6 6l5 5M22 6l-5 5M6 22l5-5M22 22l-5-5" stroke="#333" stroke-width="2"/></svg>
    <div><div class="feature-title">SUPPORT</div><div class="feature-note">Customer Service</div></div>
  </div>
</section>

<section class="section promos">
  <div class="promo-arrivals">
    <div class="promo-frame">
      <h2>NEW<br>ARRIVALS</h2>
      <p>Lorem ipsum dolor sit amet, consectetur adipiscing elit, sed do eiusmod tempor incididunt ut labore et dolore magna aliqua.</p>
      <span class="btn-light">SEE MORE</span>
    </div>
  </div>
  <div class="promo-sale" role="img" aria-label="Warm-toned photo of honey and natural ingredients">
    <div class="sale-copy">
      <h2>LATEST PRODUCT<br>25% OFF</h2>
      <p>Lorem ipsum dolor sit amet, consectetur adipiscing elit, sed do eiusmod tempor incididunt ut labore et dolore.</p>
      <span class="btn-dark">SHOP NOW</span>
    </div>
  </div>
</section>

<section class="section products">
  <div class="section-head">
    <h3><b>NEW</b> PRODUCT</h3>
    <div class="filters"><span>PRICE ▾</span><span>CATEGORY ▾</span><span>BRAND ▾</span></div>
  </div>
  <div class="product-grid">
    <article class="product-card">
      <span class="sale-badge">SALE</span>
      <div class="product-photo" role="img" aria-label="Set of nail polish bottles"></div>
      <div class="price">$ 220<s>$270.00</s></div>
      <div class="product-name">NAME OF PRODUCT</div>
      <p class="product-desc">Lorem ipsum dolor sit amet, consectetur adipiscing elit sed do eiusmod.</p>
      <div class="card-actions"><span class="act-cart dark"><svg width="18" height="16" viewBox="0 0 16 14"><path d="M1 1h3l2 8h8l1-6H5" fill="none" stroke="#fff" stroke-width="1.5"/><circle cx="7" cy="12" r="1.3" fill="#fff"/><circle cx="13" cy="12" r="1.3" fill="#fff"/></svg></span><span class="act-more">MORE</span></div>
    </article>
    <article class="product-card">
      <span class="sale-badge">SALE</span>
      <div class="product-photo" role="img" aria-label="Purple glass bottle of lotion"></div>
      <div class="price">$ 300<s>$325.00</s></div>
      <div class="product-name">NAME OF PRODUCT</div>
      <p class="product-desc">Lorem ipsum dolor sit amet, consectetur adipiscing elit sed do eiusmod.</p>
      <div class="card-actions"><span class="act-cart green"><svg width="18" height="16" viewBox="0 0 16 14"><path d="M1 1h3l2 8h8l1-6H5" fill="none" stroke="#fff" stroke-width="1.5"/><circle cx="7" cy="12" r="1.3" fill="#fff"/><circle cx="13" cy="12" r="1.3" fill="#fff"/></svg></span><span class="act-more">MORE</span></div>
    </article>
    <article class="product-card">
      <span class="sale-badge">SALE</span>
      <div class="product-photo" role="img" aria-label="Four small bottles of herbal essences"></div>
      <div class="price">$ 200<s>$225.00</s></div>
      <div class="product-name">NAME OF PRODUCT</div>
      <p class="product-desc">Lorem ipsum dolor sit amet, consectetur adipiscing elit sed do eiusmod.</p>
      <div class="card-actions"><span class="act-cart green"><svg width="18" height="16" viewBox="0 0 16 14"><path d="M1 1h3l2 8h8l1-6H5" fill="none" stroke="#fff" stroke-width="1.5"/><circle cx="7" cy="12" r="1.3" fill="#fff"/><circle cx="13" cy="12" r="1.3" fill="#fff"/></svg></span><span class="act-more">MORE</span></div>
    </article>
    <article class="product-card">
      <span class="sale-badge">SALE</span>
      <div class="product-photo" role="img" aria-label="Row of amber pharmacy jars"></div>
      <div class="price">$ 160<s>$185.00</s></div>
      <div class="product-name">NAME OF PRODUCT</div>
      <p class="product-desc">Lorem ipsum dolor sit amet, consectetur adipiscing elit sed do eiusmod.</p>
      <div class="card-actions"><span class="act-cart green"><svg width="18" height="16" viewBox="0 0 16 14"><path d="M1 1h3l2 8h8l1-6H5" fill="none" stroke="#fff" stroke-width="1.5"/><circle cx="7" cy="12" r="1.3" fill="#fff"/><circle cx="13" cy="12" r="1.3" fill="#fff"/></svg></span><span class="act-more">MORE</span></div>
    </article>
  </div>
  <div class="pager"><span class="on">1</span><span>2</span><span class="wide">Next</span></div>
</section>

<section class="section categories">
  <div class="tile tile-natural" role="img" aria-label="Dark photo of fresh herbs and leaves">
    <div class="natural-copy">
      <h4>NATURAL CARE</h4>
      <p>Lorem ipsum dolor sit amet, consectetur adipiscing elit, sed do eiusmod tempor.</p>
      <span class="btn-light">READ MORE</span>
    </div>
  </div>
  <div class="tile tile-family" role="img" aria-label="Photo of soaps and bath products with green leaves">
    <div class="tile-band">FAMILY HEALTH</div>
  </div>
  <div class="tile tile-geriatric" role="img" aria-label="Photo of golden oil bottles">
    <div class="tile-band">GERIATRIC LINE</div>
  </div>
</section>

<section class="section newsletter">
  <div class="newsletter-copy">
    <h3>Newsletter Sign Up</h3>
    <p>Lorem ipsum dolor sit amet, consectetur adipiscing elit, sed do eiusmod tempor incididunt.</p>
  </div>
  <div class="newsletter-form"><div class="news-input">Enter Your E-Mail ID</div><div class="news-btn">SUBSCRIBE</div></div>
</section>

<section class="section social">
  <h3>FOLLOW US TO STAY IN TOUCH</h3>
  <div class="social-row">
    <div class="social-item"><div class="social-btn fb"><i></i>Friendnook</div><div class="social-count">12.5K Likes</div></div>
    <div class="social-item"><div class="social-btn tw"><i></i>Chirply</div><div class="social-count">10.8K Followers</div></div>
    <div class="social-item"><div class="social-btn li"><i></i>Linkwise</div><div class="social-count">12.6K Connections</div></div>
    <div class="social-item"><div class="social-btn gp"><i></i>Circlespace</div><div class="social-count">8.3K Connections</div></div>
  </div>
</section>

<section class="section guarantees">
  <div class="guarantee">
    <svg width="32" height="28" viewBox="0 0 30 26"><path d="M3 12h6v12H3zM9 13l6-10c2 0 3 1 2 5h8c2 0 2 2 1 3l-3 11H9z" fill="none" stroke="#fff" stroke-width="2"/></svg>
    <div><b>SATISFACTION</b><b>100% GUARANTEED</b></div>
  </div>
  <div class="guarantee">
    <svg width="36" height="24" viewBox="0 0 34 22"><path d="M1 2h20v14H1zM21 7h7l5 5v4H21z" fill="#fff"/><circle cx="8" cy="18" r="3" fill="#fff" stroke="#3a2b27" stroke-width="1.5"/><circle cx="27" cy="18" r="3" fill="#fff" stroke="#3a2b27" stroke-width="1.5"/></svg>
    <div><b>FREE SHIPPING</b><b>ON ORDERS OVER $99</b></div>
  </div>
  <div class="guarantee">
    <svg width="30" height="30" viewBox="0 0 28 28"><circle cx="14" cy="14" r="11" fill="none" stroke="#fff" stroke-width="2"/><path d="M14 7v7l5 3" fill="none" stroke="#fff" stroke-width="2"/></svg>
    <div><b>7 DAY</b><b>EASY RETURN</b></div>
  </div>
</section>

<footer class="section site-footer">
  <div class="footer-col"><h5>INFORMATION</h5><ul><li>About Us</li><li>Customer Service</li><li>Privacy Policy</li><li>Search Terms</li><li>Orders and Returns</li><li>Site Map</li></ul></div>
  <div class="footer-col"><h5>WHY BUY FROM US</h5><ul><li>Shipping &amp; Returns</li><li>Secure Shopping</li><li>International Shipping</li><li>Affiliates</li><li>Group Sales</li></ul></div>
  <div class="footer-col"><h5>MY ACCOUNT</h5><ul><li>Sign In</li><li>View Cart</li><li>My Wishlist</li><li>Track My Order</li><li>Help</li></ul></div>
  <div class="footer-col"><h5>CONTACTS</h5>
    <div class="contact-line"><svg width="12" height="16" viewBox="0 0 12 16"><path d="M6 1a5 5 0 0 1 5 5c0 4-5 9-5 9S1 10 1 6a5 5 0 0 1 5-5z" fill="#bdb6b4"/><circle cx="6" cy="6" r="2" fill="#221c1b"/></svg><span>24 Calle de la Luna, 28012<br>Madrid, España</span></div>
    <div class="contact-line"><svg width="14" height="14" viewBox="0 0 14 14"><path d="M3 1l2 3-1.5 1.5a8 8 0 0 0 5 5L10 9l3 2-1 2C6 13 1 8 1 2z" fill="#bdb6b4"/></svg><span>Call Us: (000) 123-4567</span></div>
    <div class="contact-line"><svg width="14" height="12" viewBox="0 0 14 12"><path d="M1 1h12v10H1z" fill="none" stroke="#bdb6b4" stroke-width="1.4"/><path d="M1 1l6 5 6-5" fill="none" stroke="#bdb6b4" stroke-width="1.4"/></svg><span>Email: info@casalunaresweb.es</span></div>
  </div>
</footer>

<div class="section footer-bottom">
  <span>All Rights Reserved. Copyright @ 2016 Casa Lunares</span>
  <div class="cards"><span style="background:#e8e8e8"></span><span style="background:#2d6fb6"></span><span style="background:#e4a33a"></span></div>
</div>

</body>
</html>
```